VORK.
BRIDGING HORIZONS
VORK. -
Creative Brief
Use specific fonts
any thing which suits with the LOGO provided
Professional
RAJESH MOTLA
MR.
B.P. No.6213, COMMUNE-3, NEAR TORAVI LAUNDRY, KALEBA ZONE, BAMAKO-MALI
rajesh@vork.co.in
vork.co.in
pls mention MANAGING DIRECTOR, the designation, below the name of the person.
LOGO at centre. Below mentioned address at bottom: India Office D-47, Palm Enclave-II, Gurgaon, Haryana 122015 ph:+91-124-4708352, fax:+91-124-4519267 cell:+91-9871436029

```html
<!DOCTYPE html>
<html lang="en">
<head>
<meta charset="utf-8">
<title>VORK – Business Card</title>
<link rel="stylesheet" href="https://fonts.googleapis.com/css2?family=Arimo:ital,wght@0,400;0,700;1,700&display=swap">
<style>
  :root {
    --page-bg: #e9e7e4;
    --card-white: #ffffff;
    --brand-blue: #1d4f9f;
    --band-blue-light: #2a63b8;
    --band-blue-dark: #0f2f73;
    --accent-green: #7cc242;
    --accent-green-dark: #3f9a2a;
    --tagline: #1f5f7a;
    --band-text: #ffffff;
    --footer-text: rgba(255,255,255,0.85);
    --divider: rgba(255,255,255,0.7);
  }
  * { box-sizing: border-box; margin: 0; padding: 0; }
  html, body { width: 1200px; height: 780px; overflow: hidden; }
  body {
    background: var(--page-bg);
    font-family: "Arimo", Arial, sans-serif;
    position: relative;
  }
  .business-card {
    position: absolute;
    left: 150px; top: 130px;
    width: 900px; height: 520px;
    border-radius: 30px;
    overflow: hidden;
    background: var(--card-white);
    box-shadow: 0 10px 30px rgba(0,0,0,0.18);
  }
  .card-band { position: absolute; inset: 0; }
  .brand {
    position: absolute;
    left: 175px; top: 70px;
    display: flex; align-items: center; gap: 22px;
  }
  .brand-dot {
    width: 110px; height: 110px; border-radius: 50%;
    background: var(--brand-blue);
  }
  .brand-name {
    font-weight: 700;
    font-size: 96px;
    line-height: 0.9;
    letter-spacing: 2px;
    color: var(--brand-blue);
  }
  .brand-tagline {
    margin-top: 6px;
    font-weight: 700;
    font-size: 20px;
    letter-spacing: 2px;
    color: var(--tagline);
  }
  .holder {
    position: absolute;
    left: 205px; top: 326px;
    width: 215px;
    color: var(--band-text);
    text-align: right;
  }
  .holder-name { font-weight: 700; font-size: 22px; line-height: 1.15; }
  .holder-title { font-weight: 700; font-style: italic; font-size: 17px; margin-top: 4px; }
  .holder-address { font-size: 15px; line-height: 1.4; margin-top: 14px; }
  .divider {
    position: absolute;
    left: 440px; top: 330px;
    width: 2px; height: 136px;
    background: var(--divider);
  }
  .contacts {
    position: absolute;
    left: 462px; top: 326px;
    list-style: none;
    color: var(--band-text);
    font-size: 17px;
  }
  .contacts li { display: flex; align-items: center; gap: 12px; height: 35px; }
  .contacts svg { width: 20px; height: 20px; flex: none; }
  .office {
    position: absolute;
    left: 0; right: 0; top: 482px;
    text-align: center;
    color: var(--footer-text);
    font-size: 13px;
    line-height: 1.3;
  }
  .office-label { font-weight: 700; }
</style>
</head>
<body>
  <article class="business-card">
    <svg class="card-band" viewBox="0 0 900 520" preserveAspectRatio="none" aria-hidden="true">
      <defs>
        <linearGradient id="bandBlue" x1="0" y1="0" x2="0" y2="1">
          <stop offset="0" stop-color="var(--band-blue-light)"/>
          <stop offset="1" stop-color="var(--band-blue-dark)"/>
        </linearGradient>
        <linearGradient id="bandGreen" x1="0" y1="0" x2="1" y2="0">
          <stop offset="0" stop-color="var(--accent-green-dark)"/>
          <stop offset="0.5" stop-color="var(--accent-green)"/>
          <stop offset="1" stop-color="var(--accent-green-dark)"/>
        </linearGradient>
      </defs>
      <path d="M0 282 C250 255 520 308 900 228 L900 246 C520 326 250 273 0 298 Z" fill="url(#bandGreen)"/>
      <path d="M0 312 C250 285 520 336 900 258 L900 520 L0 520 Z" fill="url(#bandBlue)"/>
    </svg>

    <header class="brand">
      <span class="brand-dot"></span>
      <div>
        <div class="brand-name">VORK</div>
        <div class="brand-tagline">BRIDGING HORIZONS</div>
      </div>
    </header>

    <section class="holder">
      <p class="holder-name">Rajesh Motla</p>
      <p class="holder-title">Managing Director</p>
      <p class="holder-address">B.P. No.6213, Commune-3,<br>Near Toravi Laundry,<br>Kaleba Zone, Bamako-Mali</p>
    </section>

    <div class="divider"></div>

    <ul class="contacts">
      <li>
        <svg viewBox="0 0 24 24" fill="#fff"><path d="M6.6 10.8a15 15 0 0 0 6.6 6.6l2.2-2.2a1 1 0 0 1 1-.25 11.4 11.4 0 0 0 3.6.57 1 1 0 0 1 1 1V20a1 1 0 0 1-1 1A17 17 0 0 1 3 4a1 1 0 0 1 1-1h3.5a1 1 0 0 1 1 1c0 1.250.2 2.450.57 3.57a1 1 0 0 1-.25 1z"/></svg>
        <span>+223-20458316</span>
      </li>
      <li>
        <svg viewBox="0 0 24 24" fill="none" stroke="#fff" stroke-width="2"><rect x="7" y="2" width="10" height="20" rx="2"/><line x1="11" y1="18" x2="13" y2="18"/></svg>
        <span>+223-76204918</span>
      </li>
      <li>
        <svg viewBox="0 0 24 24" fill="none" stroke="#fff" stroke-width="2"><circle cx="12" cy="12" r="4"/><path d="M16 8v5a3 3 0 0 0 6 0v-1a10 10 0 1 0-4 8"/></svg>
        <span>rajesh@vork.co.in</span>
      </li>
      <li>
        <svg viewBox="0 0 24 24" fill="none" stroke="#fff" stroke-width="2"><circle cx="12" cy="12" r="10"/><ellipse cx="12" cy="12" rx="4" ry="10"/><line x1="2" y1="12" x2="22" y2="12"/></svg>
        <span>www.vork.co.in</span>
      </li>
    </ul>

    <footer class="office">
      <span class="office-label">India Office:</span>
      D-47, Palm Enclave-II, Gurgaon, Haryana 122015 &nbsp;·&nbsp; ph: +91-124-4708352 &nbsp;·&nbsp; fax: +91-124-4519267 &nbsp;·&nbsp; cell: +91-9871436029
    </footer>
  </article>
</body>
</html>
```